Email Signatures

I would like to create a new email signature for my team. The design will be the same for everyone, with only individual details such as name and email changing. You can also see our brand style on our website. https://www.tlmbespokehomes.com.au/

Target Market(s)

Clients for new builds or renovations

Industry/Entity Type

Construction

Colors

Designer to choose colors to be used in the design.

```html
<!DOCTYPE html>
<html lang="en">
<head>
<meta charset="utf-8">
<title>TLM Bespoke Homes – Email Signatures</title>
<link href="https://fonts.googleapis.com/css2?family=Poppins:wght@500;600;700;800&display=swap" rel="stylesheet">
<style>
  :root {
    --backdrop: #0b3a12;
    --backdrop-deep: #072a0c;
    --brand-green: #7cc242;
    --stripe-green: #3f8a2a;
    --panel-dark: #1d1d1d;
    --panel-light: #f1f1f1;
    --ink-light: #ffffff;
    --ink-dark: #161616;
    --muted-light: #d8d8d8;
    --social-dark: #4a4a4a;
    --badge-warm: #e88a1f;
    --badge-cool: #2f4a9a;
  }
  * { box-sizing: border-box; margin: 0; padding: 0; }
  html, body { width: 1200px; height: 1200px; overflow: hidden; }
  body {
    background: radial-gradient(circle at 50% 45%, var(--backdrop) 0%, var(--backdrop-deep) 100%);
    font-family: "Poppins", Arial, sans-serif;
    position: relative;
  }

  .signature {
    position: absolute;
    left: 98px;
    width: 1005px;
    height: 298px;
    overflow: hidden;
    box-shadow: 6px 8px 10px rgba(0,0,0,.55);
  }
  .signature--dark { top: 150px; }
  .signature--light { top: 764px; }

  .house-photo {
    position: absolute;
    inset: 0 400px 0 0;
    background:
      radial-gradient(ellipse at 35% 55%, rgba(255,236,200,.55) 0%, rgba(255,236,200,0) 40%),
      radial-gradient(ellipse at 62% 75%, rgba(210,140,60,.55) 0%, rgba(210,140,60,0) 35%),
      linear-gradient(160deg, #0b1424 0%, #27303c 40%, #5c5048 65%, #1b1612 100%);
  }

  .panel-shape { position: absolute; inset: 0; width: 100%; height: 100%; }
  .signature--dark .panel-fill { fill: var(--panel-dark); }
  .signature--light .panel-fill { fill: var(--panel-light); }
  .stripe-main { fill: var(--stripe-green); }
  .stripe-thin { fill: var(--brand-green); }

  .panel-watermark {
    position: absolute;
    right: -10px;
    top: 10px;
    font-size: 250px;
    font-weight: 800;
    line-height: 1;
    letter-spacing: -6px;
  }
  .signature--dark .panel-watermark { color: rgba(124,194,66,.12); }
  .signature--light .panel-watermark { color: rgba(0,0,0,.07); }

  .brand-name {
    position: absolute;
    left: 12px;
    top: 6px;
    color: var(--ink-light);
    font-weight: 700;
    line-height: 1;
  }
  .brand-name__initials { display: block; font-size: 84px; letter-spacing: 2px; }
  .brand-name__words { display: block; font-size: 33px; margin-top: 6px; }

  .award-badge {
    position: absolute;
    left: 13px;
    top: 203px;
    width: 60px;
    height: 91px;
    background: linear-gradient(90deg, var(--badge-warm) 0 55%, var(--badge-cool) 55% 100%);
  }
  .awards {
    position: absolute;
    top: 254px;
    display: flex;
    gap: 14px;
    left: 91px;
    color: var(--muted-light);
    font-size: 9.5px;
    font-weight: 600;
    line-height: 1.35;
  }
  .award__title { color: var(--ink-light); font-size: 10.5px; }
  .award__title::before { content: "• "; color: var(--brand-green); }

  .contact-list { position: absolute; inset: 0; list-style: none; }
  .contact-item {
    position: absolute;
    display: flex;
    align-items: center;
    gap: 14px;
    font-size: 18.5px;
    font-weight: 600;
    white-space: nowrap;
  }
  .contact-item svg { width: 30px; height: 30px; flex: none; }
  .signature--dark .contact-item { color: var(--ink-light); }
  .signature--dark .contact-item svg { fill: var(--brand-green); }
  .signature--light .contact-item { color: var(--ink-dark); }
  .signature--light .contact-item svg { fill: var(--ink-dark); }
  .contact-item--phone { left: 566px; top: 37px; }
  .contact-item--email { left: 554px; top: 84px; }
  .contact-item--web { left: 542px; top: 131px; }
  .contact-item--place { left: 528px; top: 184px; }

  .social-row {
    position: absolute;
    top: 265px;
    left: 617px;
    display: flex;
    gap: 49px;
  }
  .social-link { width: 25px; height: 25px; border-radius: 4px; }
  .signature--dark .social-link { background: var(--social-dark); }
  .signature--light .social-link { background: #b9b9b9; }
</style>
</head>
<body>

<!-- Dark variant -->
<section class="signature signature--dark" aria-label="Email signature, dark version">
  <div class="house-photo" role="img" aria-label="Photo of a modern two-storey home lit at dusk with timber cladding"></div>
  <svg class="panel-shape" viewBox="0 0 1005 298" preserveAspectRatio="none" aria-hidden="true">
    <polygon class="panel-fill" points="560,0 1005,0 1005,298 470,298"/>
    <polygon class="stripe-main" points="548,0 556,0 466,298 456,298"/>
    <polygon class="stripe-thin" points="506,40 510,40 440,298 436,298"/>
  </svg>
  <div class="panel-watermark" aria-hidden="true">TLM</div>

  <h1 class="brand-name">
    <span class="brand-name__initials">TLM</span>
    <span class="brand-name__words">BESPOKE HOMES</span>
  </h1>
  <div class="award-badge" aria-hidden="true"></div>
  <div class="awards">
    <p class="award"><span class="award__title">BUILDERS GUILD TASMANIA</span><br>FINALIST 2021. 2023.2024<br>WINNER 2022. 2023. 2024</p>
    <p class="award"><span class="award__title">BUILDERS GUILD AUSTRALIA</span><br>FINALIST 2022. 2023.2024</p>
  </div>

  <ul class="contact-list">
    <li class="contact-item contact-item--phone"><svg viewBox="0 0 24 24"><path d="M6.6 10.8a15.1 15.1 0 0 0 6.6 6.6l2.2-2.2c.3-.3.7-.4 1-.2 1.1.4 2.3.6 3.6.6.6 0 1 .4 1 1V20c0 .6-.4 1-1 1A17 17 0 0 1 3 4c0-.6.4-1 1-1h3.5c.6 0 1 .4 1 1 0 1.3.2 2.5.6 3.6.1.3 0 .7-.2 1z"/></svg>0412555019</li>
    <li class="contact-item contact-item--email"><svg viewBox="0 0 24 24"><path d="M2 5h20v14H2z M2 5l10 8 10-8" /></svg>info@tlmbespokehomes.com.au</li>
    <li class="contact-item contact-item--web"><svg viewBox="0 0 24 24"><path fill-rule="evenodd" d="M12 2a10 10 0 1 1 0 20 10 10 0 0 1 0-20zm-1 2.1A8 8 0 0 0 4.1 11H8c.1-2.6.9-5 3-6.9zm2 0c2.1 1.9 2.9 4.3 3 6.9h3.9A8 8 0 0 0 13 4.1zM10 11h4c-.1-2.2-.8-4.1-2-5.5-1.2 1.4-1.9 3.3-2 5.5zm-5.9 2A8 8 0 0 0 11 19.9c-2.1-1.9-2.9-4.3-3-6.9zm5.9 0c.1 2.2.8 4.1 2 5.5 1.2-1.4 1.9-3.3 2-5.5zm6 0c-.1 2.6-.9 5-3 6.9a8 8 0 0 0 6.9-6.9z"/></svg>www.tlmbespokehomes.com.au</li>
    <li class="contact-item contact-item--place"><svg viewBox="0 0 24 24"><path d="M12 2a7 7 0 0 0-7 7c0 5 7 13 7 13s7-8 7-13a7 7 0 0 0-7-7zm0 9.5a2.5 2.5 0 1 1 0-5 2.5 2.5 0 0 1 0 5z"/></svg>Banksia Place, Rosebud</li>
  </ul>
  <nav class="social-row" aria-label="Social profiles">
    <span class="social-link"></span><span class="social-link"></span><span class="social-link"></span><span class="social-link"></span>
  </nav>
</section>

<!-- Light variant -->
<section class="signature signature--light" aria-label="Email signature, light version">
  <div class="house-photo" role="img" aria-label="Photo of a modern two-storey home lit at dusk with timber cladding"></div>
  <svg class="panel-shape" viewBox="0 0 1005 298" preserveAspectRatio="none" aria-hidden="true">
    <polygon class="panel-fill" points="560,0 1005,0 1005,298 470,298"/>
    <polygon class="stripe-main" points="548,0 556,0 466,298 456,298"/>
    <polygon class="stripe-thin" points="506,40 510,40 440,298 436,298"/>
  </svg>
  <div class="panel-watermark" aria-hidden="true">TLM</div>

  <h2 class="brand-name">
    <span class="brand-name__initials">TLM</span>
    <span class="brand-name__words">BESPOKE HOMES</span>
  </h2>
  <div class="award-badge" aria-hidden="true"></div>
  <div class="awards">
    <p class="award"><span class="award__title">BUILDERS GUILD TASMANIA</span><br>FINALIST 2021. 2023.2024<br>WINNER 2022. 2023. 2024</p>
    <p class="award"><span class="award__title">BUILDERS GUILD AUSTRALIA</span><br>FINALIST 2022. 2023.2024</p>
  </div>

  <ul class="contact-list">
    <li class="contact-item contact-item--phone"><svg viewBox="0 0 24 24"><path d="M6.6 10.8a15.1 15.1 0 0 0 6.6 6.6l2.2-2.2c.3-.3.7-.4 1-.2 1.1.4 2.3.6 3.6.6.6 0 1 .4 1 1V20c0 .6-.4 1-1 1A17 17 0 0 1 3 4c0-.6.4-1 1-1h3.5c.6 0 1 .4 1 1 0 1.3.2 2.5.6 3.6.1.3 0 .7-.2 1z"/></svg>0412555019</li>
    <li class="contact-item contact-item--email"><svg viewBox="0 0 24 24"><path d="M2 5h20v14H2z M2 5l10 8 10-8" /></svg>info@tlmbespokehomes.com.au</li>
    <li class="contact-item contact-item--web"><svg viewBox="0 0 24 24"><path fill-rule="evenodd" d="M12 2a10 10 0 1 1 0 20 10 10 0 0 1 0-20zm-1 2.1A8 8 0 0 0 4.1 11H8c.1-2.6.9-5 3-6.9zm2 0c2.1 1.9 2.9 4.3 3 6.9h3.9A8 8 0 0 0 13 4.1zM10 11h4c-.1-2.2-.8-4.1-2-5.5-1.2 1.4-1.9 3.3-2 5.5zm-5.9 2A8 8 0 0 0 11 19.9c-2.1-1.9-2.9-4.3-3-6.9zm5.9 0c.1 2.2.8 4.1 2 5.5 1.2-1.4 1.9-3.3 2-5.5zm6 0c-.1 2.6-.9 5-3 6.9a8 8 0 0 0 6.9-6.9z"/></svg>www.tlmbespokehomes.com.au</li>
    <li class="contact-item contact-item--place"><svg viewBox="0 0 24 24"><path d="M12 2a7 7 0 0 0-7 7c0 5 7 13 7 13s7-8 7-13a7 7 0 0 0-7-7zm0 9.5a2.5 2.5 0 1 1 0-5 2.5 2.5 0 0 1 0 5z"/></svg>Banksia Place, Rosebud</li>
  </ul>
  <nav class="social-row" aria-label="Social profiles">
    <span class="social-link"></span><span class="social-link"></span><span class="social-link"></span><span class="social-link"></span>
  </nav>
</section>

</body>
</html>
```